Icon and color palette for a math game

We are in development of a mathematics game, and need a fresh and engaging icon and text logo (logotype/word mark) and splash screen. We would also like suggestions for a colour palette.

The main element in the project is the icon. We need an icon that says something about what the game is all about. We have uploaded a sketch for your inspiration.

The game is about challenging your friends to see who can create the most calculations based on numbers and operations (+ and -) that are presented to you. The name of the game is Digitclash.

Attached are some images for inspiration:
Updates

Project Deadline Extended
Reason: Deadline is extended due to christmas holidays. We'll be slow at responding the upcoming days.

Target Market(s)

Children and grown-ups that like to play games and challenge each other.

Requirements
Must have
• - iOS app icons
- Android app icons
- Windows phone app icons
- Text logo
- Splash screen (the screen that is shown while the game loads)
- Color palette
- Example of the two images attached with the new palette

```html
<!DOCTYPE html>
<html lang="en">
<head>
<meta charset="utf-8">
<title>Tile Palette and Game Board</title>
<link href="https://fonts.googleapis.com/css2?family=Nunito+Sans:wght@300;400;700&display=swap" rel="stylesheet">
<style>
  :root {
    --pink: #f9a0e4;
    --purple: #b8a0e8;
    --green: #bddb72;
    --tan: #dbb679;
    --blue: #378fca;
    --tile: #f2f2f2;
    --frame: #e0e0e0;
    --footer: #e6e6e6;
    --field: #a9a9a9;
    --label: #8a8a8a;
    --white: #ffffff;
    --ink: #222222;
  }
  html, body {
    margin: 0;
    padding: 0;
    overflow: hidden;
    background: var(--white);
  }
  .canvas {
    position: relative;
    width: 1200px;
    height: 927px;
    overflow: hidden;
    background: var(--white);
    font-family: "Nunito Sans", sans-serif;
  }
  .swatch, .tile {
    position: absolute;
    width: 91px;
    height: 91px;
    border-radius: 10px;
  }
  .swatch--lifted, .tile--raised {
    box-shadow: 0 2px 7px rgba(0, 0, 0, 0.38);
  }
  .pink { background: var(--pink); --accent: var(--pink); }
  .purple { background: var(--purple); --accent: var(--purple); }
  .green { background: var(--green); --accent: var(--green); }
  .tan { background: var(--tan); --accent: var(--tan); }

  .badge {
    position: absolute;
    right: -16px;
    top: -7px;
    width: 30px;
    height: 30px;
    border-radius: 50%;
    background: var(--white);
    border: 4px solid var(--accent);
    display: flex;
    align-items: center;
    justify-content: center;
    font-size: 17px;
    font-weight: 400;
    color: var(--ink);
    letter-spacing: 2px;
    text-indent: 2px;
    line-height: 1;
  }

  .legend {
    position: absolute;
    left: 40px;
    top: 714px;
    margin: 0;
    padding: 0;
    list-style: none;
    font-size: 33px;
    font-weight: 300;
    color: var(--label);
    line-height: 47px;
  }

  .phone {
    position: absolute;
    left: 607px;
    top: 42px;
    width: 563px;
    height: 852px;
    box-sizing: border-box;
    border: 1px solid var(--frame);
    border-top: none;
  }
  .phone__header {
    position: absolute;
    left: -1px;
    right: -1px;
    top: 0;
    height: 95px;
    background: var(--blue);
  }
  .phone__player {
    position: absolute;
    top: 18px;
    width: 56px;
    height: 56px;
    border: 3px solid var(--white);
    border-radius: 50%;
  }
  .phone__player--left { left: 18px; }
  .phone__player--right { right: 11px; }
  .phone__score {
    position: absolute;
    left: 0;
    right: 0;
    top: 27px;
    text-align: center;
    color: var(--white);
    font-size: 36px;
    font-weight: 300;
    line-height: 40px;
  }
  .equation {
    position: absolute;
    left: 54px;
    top: 144px;
    width: 474px;
    height: 52px;
    box-sizing: border-box;
    border: 3px solid var(--field);
  }
  .equation__result {
    position: absolute;
    right: 93px;
    top: 4px;
    font-size: 31px;
    font-weight: 300;
    color: var(--label);
    line-height: 40px;
  }
  .equation__toggle {
    position: absolute;
    right: 6px;
    top: 5px;
    width: 60px;
    height: 36px;
    border-radius: 18px;
    background: var(--field);
  }
  .phone__footer {
    position: absolute;
    left: -1px;
    right: -1px;
    bottom: 0;
    height: 38px;
    background: var(--footer);
  }
  .board .tile { background: var(--tile); }
  .board .tile.green { background: var(--green); }
  .board .tile.pink { background: var(--pink); }
</style>
</head>
<body>
<main class="canvas">

  <section class="palette" aria-label="Colour palette">
    <div class="swatch pink" style="left:14px;top:150px"></div>
    <div class="swatch purple" style="left:14px;top:257px"></div>
    <div class="swatch green" style="left:14px;top:365px"></div>
    <div class="swatch tan" style="left:14px;top:472px"></div>

    <div class="swatch pink" style="left:199px;top:116px"><span class="badge">×2</span></div>
    <div class="swatch purple" style="left:202px;top:251px"><span class="badge">×3</span></div>
    <div class="swatch green" style="left:202px;top:374px"><span class="badge">?2</span></div>
    <div class="swatch tan" style="left:201px;top:529px"><span class="badge">?3</span></div>

    <div class="swatch swatch--lifted pink" style="left:366px;top:116px"><span class="badge">×2</span></div>
    <div class="swatch swatch--lifted purple" style="left:368px;top:250px"><span class="badge">×3</span></div>
    <div class="swatch swatch--lifted green" style="left:368px;top:374px"><span class="badge">?2</span></div>
    <div class="swatch swatch--lifted tan" style="left:366px;top:529px"><span class="badge">?3</span></div>
  </section>

  <ul class="legend">
    <li>Double Number</li>
    <li>Triple Number</li>
    <li>Double Calculation</li>
    <li>Triple Calculation</li>
  </ul>

  <section class="phone" aria-label="Game board screen">
    <header class="phone__header">
      <span class="phone__player phone__player--left"></span>
      <span class="phone__score">10</span>
      <span class="phone__player phone__player--right"></span>
    </header>

    <div class="equation">
      <span class="equation__result">= 0</span>
      <span class="equation__toggle"></span>
    </div>

    <div class="board">
      <div class="tile" style="left:82px;top:247px"></div>
      <div class="tile" style="left:190px;top:247px"></div>
      <div class="tile" style="left:295px;top:247px"></div>
      <div class="tile" style="left:403px;top:247px"></div>

      <div class="tile tile--raised green" style="left:82px;top:354px"><span class="badge">?2</span></div>
      <div class="tile" style="left:190px;top:354px"></div>
      <div class="tile tile--raised" style="left:295px;top:354px"></div>
      <div class="tile" style="left:403px;top:354px"></div>

      <div class="tile" style="left:82px;top:461px"></div>
      <div class="tile" style="left:190px;top:461px"></div>
      <div class="tile" style="left:295px;top:461px"></div>
      <div class="tile tile--raised" style="left:403px;top:461px"></div>

      <div class="tile" style="left:82px;top:566px"></div>
      <div class="tile" style="left:190px;top:566px"></div>
      <div class="tile" style="left:295px;top:566px"></div>
      <div class="tile" style="left:403px;top:566px"></div>

      <div class="tile" style="left:82px;top:672px"></div>
      <div class="tile tile--raised" style="left:190px;top:672px"></div>
      <div class="tile" style="left:295px;top:672px"></div>
      <div class="tile pink" style="left:403px;top:672px"><span class="badge">×2</span></div>
    </div>

    <footer class="phone__footer"></footer>
  </section>

</main>
</body>
</html>
```